Kestrel Building Works Business Card and more!

We need a business card design for Kestrel Building Works Ltd, a respected building company that specialises in high quality designer homes.

We're after a sleek, clean, modern business card that incorporates our new logo (see attached) and colours, with black being the background.

We are Certified Trade Craftsmen and need to include their logo (see attached) on our cards, balancing but not taking over our logo.

Details to be included:

Warren Pike
Director

Phone: 0219462513
Email: kestrelbuild.nz@mailbox-example.nz
Website: www.kestrelbuildingworks.co.nz

Additional Information

A start up website is also under construction and needing attention and letterheads are needed!

We look forward to your designs!

Target Market(s)

30+ people who are interested in building new or renovating current homes

Industry/Entity Type

Construction

Contact Information for Business Card

Warren Pike
Director

Phone: 0219462513
Facebook: www.socialpage-example.com/kestrelbuild.nz

Font styles to use
Serif

Colors

Designer to choose colors to be used in the design.

Requirements
Must have
• Our new logo
• Our colours
• ctc logo

```html
<!DOCTYPE html>
<html lang="en">
<head>
<meta charset="utf-8">
<title>Kestrel Building Works – Business Card</title>
<link rel="stylesheet" href="https://fonts.googleapis.com/css2?family=Cinzel:wght@400;700&family=Lato:wght@400;700&display=swap">
<style>
  :root {
    --backdrop: #d9d9d9;
    --card: #111111;
    --texture-light: #222222;
    --texture-dark: #0b0b0b;
    --gold: #c9a15a;
    --white: #f4f1ea;
    --muted: #cfcac0;
    --badge: #ecebe8;
    --serif: "Cinzel", "Times New Roman", serif;
    --sans: "Lato", Arial, sans-serif;
  }
  * { margin: 0; padding: 0; box-sizing: border-box; }
  html, body { width: 1200px; height: 919px; overflow: hidden; }
  body {
    background: var(--backdrop);
    position: relative;
  }
  .card {
    position: absolute;
    top: 182px;
    width: 340px;
    height: 556px;
    background: var(--card);
    border-radius: 3px;
    color: var(--white);
    overflow: hidden;
  }
  .card--front { left: 220px; }
  .card--back { left: 640px; }

  /* Front */
  .front-texture {
    position: absolute;
    inset: 0;
    background:
      radial-gradient(ellipse at 30% 20%, var(--texture-light) 0%, transparent 60%),
      radial-gradient(ellipse at 75% 80%, var(--texture-light) 0%, transparent 55%),
      linear-gradient(160deg, #1a1a1a 0%, var(--texture-dark) 100%);
  }
  .front-brand {
    position: absolute;
    top: 168px;
    left: 0;
    right: 0;
    text-align: center;
  }
  .front-brand__mark {
    display: block;
    width: 44px;
    height: 44px;
    margin: 0 auto 22px;
    border-radius: 50%;
    background: var(--gold);
  }
  .front-brand__name {
    font-family: var(--serif);
    font-weight: 400;
    color: var(--white);
    font-size: 31px;
    line-height: 1.2;
    letter-spacing: 2.5px;
    text-transform: uppercase;
  }
  .trade-badge {
    position: absolute;
    left: 50%;
    top: 372px;
    width: 110px;
    height: 110px;
    margin-left: -55px;
    border-radius: 50%;
    background: var(--badge);
  }

  /* Back */
  .back-brand {
    position: absolute;
    top: 92px;
    left: 40px;
    display: flex;
    align-items: center;
    gap: 12px;
  }
  .back-brand__mark {
    width: 22px;
    height: 22px;
    border-radius: 50%;
    background: var(--gold);
  }
  .back-brand__name {
    font-family: var(--serif);
    font-weight: 400;
    font-size: 16px;
    letter-spacing: 1.5px;
    text-transform: uppercase;
    color: var(--white);
  }
  .person {
    position: absolute;
    top: 340px;
    left: 40px;
  }
  .person__name {
    font-family: var(--serif);
    font-weight: 700;
    font-size: 18px;
    letter-spacing: 0.5px;
    text-transform: uppercase;
  }
  .person__role {
    font-family: var(--sans);
    font-weight: 700;
    font-size: 9px;
    letter-spacing: 1px;
    text-transform: uppercase;
    margin-top: 4px;
    margin-left: 2px;
  }
  .contact {
    position: absolute;
    top: 404px;
    left: 40px;
    padding-left: 10px;
    border-left: 3px solid var(--gold);
    list-style: none;
    font-family: var(--sans);
    font-size: 10px;
    line-height: 1.6;
    color: var(--muted);
  }
</style>
</head>
<body>

  <section class="card card--front" aria-label="Business card front">
    <div class="front-texture" role="img" aria-label="Subtle repeating monogram pattern in dark tones across the card"></div>
    <div class="front-brand">
      <span class="front-brand__mark"></span>
      <p class="front-brand__name">Kestrel<br>Building Works</p>
    </div>
    <div class="trade-badge" role="img" aria-label="Certified Trade Craftsmen badge"></div>
  </section>

  <section class="card card--back" aria-label="Business card back">
    <div class="back-brand">
      <span class="back-brand__mark"></span>
      <span class="back-brand__name">Kestrel Building Works</span>
    </div>
    <div class="person">
      <p class="person__name">Warren Pike</p>
      <p class="person__role">Director</p>
    </div>
    <ul class="contact">
      <li>0219462513</li>
      <li>kestrelbuild.nz@mailbox-example.nz</li>
      <li>www.kestrelbuildingworks.co.nz</li>
      <li>www.socialpage-example.com/kestrelbuild.nz</li>
    </ul>
  </section>

</body>
</html>
```